Beauty Salon Design

The business card design will be for a new beauty salon opening up.

The therapist has over 11 years at a leading beauty Salon in perth.

The two colours that the salon will use is black and gold.

Industry/Entity Type

Beauty Salon

Contact Information for Business Card

Lumora Beauty

Corinne Halstead Pryce
Advanced beauty therapist
0455 817 302

Monday - Friday 9am - 2.30pm
Weekends and nights by appointment only

Waxing, Tinting, Swedish massage, hot stone massage, facials, peels, micro, LED light treatment, skin needling and retail products.

```html
<!DOCTYPE html>
<html lang="en">
<head>
<meta charset="UTF-8">
<title>Lumora Beauty – Business Card</title>
<link rel="stylesheet" href="https://fonts.googleapis.com/css2?family=Quicksand:wght@400;500;600&display=swap">
<style>
  :root {
    --page-bg: #ffffff;
    --gold-light: #f8ecaa;
    --gold-mid: #e2c872;
    --gold-deep: #b8923a;
    --gold-text: #d8b85a;
    --gold-soft: #c9aa5a;
    --black: #0c0c0c;
    --black-soft: #1d1d1d;
    --accent-red: #7a1616;
    --ink: #1a130a;
  }
  * { box-sizing: border-box; margin: 0; padding: 0; }
  html, body {
    width: 1200px; height: 900px; overflow: hidden;
    background: var(--page-bg);
    font-family: "Quicksand", "Helvetica Neue", Arial, sans-serif;
  }
  .canvas { position: relative; width: 1200px; height: 900px; }
  .card {
    position: absolute; top: 295px;
    width: 540px; height: 310px;
    border-radius: 24px; overflow: hidden;
    background: var(--black);
    box-shadow: 0 14px 30px rgba(0,0,0,0.22);
  }
  .card--front { left: 40px; }
  .card--back { left: 620px; }

  .damask {
    position: absolute; inset: 0;
    background:
      radial-gradient(ellipse at 50% 40%, var(--black-soft) 0%, var(--black) 75%);
  }

  /* Front */
  .gold-panel {
    position: absolute; left: 0; top: 0; width: 100%; height: 190px;
    background: linear-gradient(100deg, var(--gold-deep) 0%, var(--gold-mid) 30%, var(--gold-light) 55%, var(--gold-mid) 80%, var(--gold-deep) 100%);
  }
  .accent-rule {
    position: absolute; left: 0; top: 190px; width: 100%; height: 4px;
    background: var(--accent-red);
  }
  .brand {
    position: absolute; left: 0; top: 0; width: 100%; height: 190px;
    display: flex; align-items: center; justify-content: center; gap: 14px;
  }
  .brand-dot {
    width: 16px; height: 16px; border-radius: 50%;
    background: var(--ink);
  }
  .brand-name {
    font-size: 42px; font-weight: 500; color: var(--ink);
    letter-spacing: 1px;
  }
  .contact {
    position: absolute; left: 0; top: 194px; width: 100%; height: 116px;
    display: flex; flex-direction: column; align-items: center; justify-content: center;
    color: var(--gold-text);
  }
  .contact-name { font-size: 21px; font-weight: 500; letter-spacing: 0.5px; }
  .contact-role { font-size: 15px; color: var(--gold-soft); margin-top: 2px; }
  .contact-phone { font-size: 23px; font-weight: 500; letter-spacing: 4px; margin-top: 12px; }

  /* Back */
  .back-content {
    position: absolute; inset: 0;
    display: flex; flex-direction: column; align-items: center;
    padding: 62px 36px 0; text-align: center; color: var(--gold-text);
  }
  .hours { font-size: 19px; font-weight: 500; line-height: 1.4; }
  .services {
    margin-top: 54px; font-size: 14.5px; line-height: 1.45; color: var(--gold-soft);
  }
</style>
</head>
<body>
<main class="canvas">
  <section class="card card--front" aria-label="Business card front">
    <div class="damask" role="img" aria-label="Black damask pattern background"></div>
    <div class="gold-panel"></div>
    <div class="accent-rule"></div>
    <div class="brand">
      <span class="brand-dot"></span>
      <span class="brand-name">Lumora Beauty</span>
    </div>
    <div class="contact">
      <p class="contact-name">Corinne Halstead Pryce</p>
      <p class="contact-role">Advanced beauty therapist</p>
      <p class="contact-phone">0455 817 302</p>
    </div>
  </section>

  <section class="card card--back" aria-label="Business card back">
    <div class="damask" role="img" aria-label="Black damask pattern background"></div>
    <div class="back-content">
      <p class="hours">Monday - Friday 9am - 2.30pm<br>Weekends and nights by appointment only</p>
      <p class="services">Waxing, Tinting, Swedish massage, hot stone massage,<br>facials, peels, micro, LED light treatment, skin needling<br>and retail products.</p>
    </div>
  </section>
</main>
</body>
</html>
```